The Hollowmere Stillhouse - Gin Bottle Label

Hi Designers,

We are currently looking for some fresh ideas regarding a label for our gin bottle. We are relatively small and with an emphasis on a quality tipple
made from the very finest and responsibly sourced botanicals. Our operation concentrates on small batch/hand crafted in its purest sense and we would like to reflect this in our brand.
We are looking for a label to read The Hollowmere Stillhouse and have feminine accents with a primary background colour similar to Wrenfield green/blue. Things like Sakura branches with blossom, floral, pretty scrolling perhaps around either full or partial boarder. Gold foil might be used to accent the black border/highlight the word "Hollowmere" and perhaps any floral pattern.
There could reconsideration given to include two boxes "Batch No" and "Bottle No" which would remain empty and filled out by hand during bottling.
Our gin will be 45%ABV
Some floral designs might look good as though they were watercolours in appearance perhaps.
Our bottles are clear medicine style of which I shall attatch a pic.
We are pretty excited about this and would invite anyone with flair and great ideas to have fun with this design.

With kind regards,

Max

Target Market(s)

People who adore bespoke Gin and would be predominately female.

Colors
86cfc6

Requirements
Must have
• We love the Wrenfield green tones and this well may be our label colour with your design.
• The Hollowmere Stillhouse - Gin - 45ABV
Nice to have
• Batch No & Bottle No boxes

```html
<!DOCTYPE html>
<html lang="en">
<head>
<meta charset="utf-8">
<title>The Hollowmere Stillhouse – Gin Label</title>
<link href="https://fonts.googleapis.com/css2?family=Cinzel:wght@400;600&family=Exo+2:ital,wght@1,800&family=Oswald:wght@400&family=Roboto+Condensed:wght@400&display=swap" rel="stylesheet">
<style>
  :root {
    --page: #f4f4f4;
    --label-teal: #a9dcd9;
    --gin-teal: #8fd3cd;
    --panel: #ffffff;
    --gold: #e9cf3c;
    --blossom-pink: #f3c3d6;
    --blossom-deep: #e48ab0;
    --brand-pink: #e0649c;
    --ink: #4a4a4a;
  }
  * { margin: 0; padding: 0; box-sizing: border-box; }
  html, body { width: 1200px; height: 1106px; overflow: hidden; background: var(--page); }

  .label {
    position: absolute;
    left: 170px; top: 90px;
    width: 860px; height: 927px;
    background: var(--label-teal);
    overflow: hidden;
  }
  .panel {
    position: absolute;
    left: 136px; top: 148px;
    width: 576px; height: 636px;
    background: var(--panel);
  }
  .blossom {
    position: absolute;
    z-index: 2;
  }
  .blossom--top-left {
    left: 0; top: 0; width: 560px; height: 300px;
    background:
      radial-gradient(ellipse 55% 35% at 45% 15%, var(--blossom-pink) 0%, rgba(243,195,214,0.7) 45%, rgba(243,195,214,0) 100%),
      radial-gradient(ellipse 18% 55% at 8% 60%, rgba(228,138,176,0.8) 0%, rgba(243,195,214,0) 100%);
  }
  .blossom--bottom-right {
    right: 0; bottom: 0; width: 520px; height: 320px;
    background:
      radial-gradient(ellipse 55% 30% at 55% 90%, var(--blossom-pink) 0%, rgba(243,195,214,0.7) 45%, rgba(243,195,214,0) 100%),
      radial-gradient(ellipse 16% 50% at 92% 45%, rgba(228,138,176,0.8) 0%, rgba(243,195,214,0) 100%);
  }
  .gold-frame {
    position: absolute;
    left: 99px; top: 104px;
    width: 650px; height: 721px;
    border: 4px solid var(--gold);
    z-index: 3;
  }
  .brand__name {
    position: absolute;
    left: 162px; top: 228px;
    z-index: 4;
    font-family: "Cinzel", serif;
    font-weight: 600;
    font-size: 52px;
    line-height: 1;
    color: var(--brand-pink);
    white-space: nowrap;
  }
  .brand__house {
    position: absolute;
    left: 440px; top: 336px;
    z-index: 4;
    font-family: "Cinzel", serif;
    font-weight: 400;
    font-size: 34px;
    line-height: 1;
    color: var(--ink);
    letter-spacing: 1px;
    white-space: nowrap;
  }
  .product {
    position: absolute;
    left: 0; top: 430px; width: 100%;
    z-index: 4;
    text-align: center;
    font-family: "Exo 2", sans-serif;
    font-style: italic;
    font-weight: 800;
    font-size: 160px;
    line-height: 1;
    color: var(--gin-teal);
    letter-spacing: 6px;
  }
  .tagline {
    position: absolute;
    left: 0; top: 602px; width: 100%;
    z-index: 4;
    text-align: center;
    font-family: "Roboto Condensed", sans-serif;
    font-size: 24px;
    line-height: 30px;
    color: var(--ink);
    letter-spacing: 1px;
  }
  .strength {
    position: absolute;
    left: 0; top: 692px; width: 100%;
    z-index: 4;
    text-align: center;
    font-family: "Oswald", sans-serif;
    font-size: 40px;
    line-height: 50px;
    color: var(--ink);
    letter-spacing: 3px;
  }
</style>
</head>
<body>
  <main class="label">
    <div class="panel"></div>
    <div class="blossom blossom--top-left" role="img" aria-label="Watercolour sakura branch with pink blossoms reaching in from the top-left corner"></div>
    <div class="blossom blossom--bottom-right" role="img" aria-label="Watercolour sakura branch with pink blossoms reaching in from the bottom-right corner"></div>
    <div class="gold-frame"></div>

    <h1 class="brand">
      <span class="brand__name">Hollowmere</span>
      <span class="brand__house">Stillhouse</span>
    </h1>
    <p class="product">GIN</p>
    <p class="tagline">THE FINEST SMALL BATCH HAND CRAFTED</p>
    <p class="strength">45%ABV</p>
  </main>
</body>
</html>
```